Birch Ledger brochure to showcase Masonry, landscape and concrete services

SEE RECENT COMMENT PAGE FOR BEST INFO We need a brochure designed to help inform our clients of our services and give them information on the pitfalls in the masonry, landscape and Hardscape industry, including drainage and frost protection, showcase some of our work we like to make all our material for marketing geared toward helping the client learn something. Drainage on any site is the number one component to a successful landscape, Hardscape and outdoor living area. This is often and overlooked to get to the stuff that's fun in turn, causing failure from frost due to northern Minnesota's harsh climate. Creating many disappointments on a large investment project. The brochure should also have a section focused on masonry, including fireplaces chimney repair, stucco repair, stone and brick. Some of the language should be editable. I will attach pictures and our logo.

Target Market(s)

Older customers with dual income looking to update and add outdoor living

Industry/Entity Type

Masonry, landscape, concrete, outdoor living

Font styles to use
Serif
Sans Serif
Other font styles liked:
• Arial

Colors

Designer to choose only greyscale colors for use in the design.

Requirements
Must have
• I really like gray, silver and black when I do marketing mixed with White, but I thought adding some greenery for the landscape portion might look good too on this brochure
Nice to have
• I do not like it too busy so keep it clean and simple
Should not have
• Tons of clutter, tons of words, hard to read and look at

```html
<!DOCTYPE html>
<html lang="en">
<head>
<meta charset="utf-8">
<title>Birch Ledger Brochure</title>
<link href="https://fonts.googleapis.com/css2?family=Poppins:wght@300;400;500;600;700&display=swap" rel="stylesheet">
<style>
:root{
  --page-bg:#dfe9f7;
  --paper:#ffffff;
  --ink:#1c1c1c;
  --ink-soft:#555555;
  --charcoal:#2f2f2f;
  --slate:#5c5c5c;
  --silver:#b9b9b9;
  --mist:#e7e7e7;
  --moss:#5f7a4e;
}
*{margin:0;padding:0;box-sizing:border-box}
html,body{width:874px;height:1200px;overflow:hidden}
body{background:var(--page-bg);font-family:"Poppins",Arial,sans-serif;color:var(--ink);position:relative}
.sheet{position:absolute;left:24px;width:826px;background:var(--paper);display:flex;box-shadow:0 4px 14px rgba(0,0,0,.18)}
.sheet--outside{top:22px;height:432px}
.sheet--inside{top:476px;height:704px}
.panel{position:relative;width:275.33px;height:100%;overflow:hidden}
.photo{position:absolute;display:block}

/* outside: masonry panel */
.masonry .eyebrow{position:absolute;left:18px;top:18px;font-size:17px;font-weight:400;line-height:1}
.masonry .title{position:absolute;left:18px;top:38px;font-size:31px;font-weight:700;line-height:1}
.masonry .sub{position:absolute;left:18px;top:72px;font-size:17px;font-weight:400;line-height:1}
.service-list{position:absolute;left:18px;top:102px;list-style:none;font-size:7px;line-height:11px;color:var(--ink-soft)}
.service-list li::before{content:"•";margin-right:4px}
.masonry .photo{left:0;top:176px;width:100%;height:256px;background:linear-gradient(160deg,#6b6258,#2c2a28 60%,#4a5a3e)}

/* outside: craftsmanship panel */
.craft{background:linear-gradient(180deg,#3b3b3b,#2a2a2a 60%,#3d3d3d)}
.craft .photo--top{left:16px;top:16px;width:243px;height:96px;background:linear-gradient(180deg,#8a9aa8,#4f5a45 55%,#7a6f62)}
.craft .tagline{position:absolute;left:16px;right:16px;top:120px;text-align:center;color:var(--paper);font-size:9px;font-weight:500}
.craft .photo--mid{left:16px;top:144px;width:243px;height:122px;background:linear-gradient(180deg,#a9a49b,#6e6a62 50%,#4d4a45)}
.craft .motto{position:absolute;right:34px;top:296px;color:var(--paper);font-size:15px;font-weight:500;line-height:22px;text-align:left}
.craft .motto svg{vertical-align:-2px;margin-right:4px}
.craft .web{position:absolute;left:0;right:0;top:388px;text-align:center;color:var(--silver);font-size:9px;letter-spacing:.3px}

/* outside: natural elements panel */
.natural .heading{position:absolute;right:18px;top:16px;text-align:right;line-height:1.05}
.natural .heading span{display:block;font-size:21px;font-weight:400}
.natural .heading strong{display:block;font-size:29px;font-weight:700}
.brand{position:absolute;right:18px;top:92px;width:92px;height:42px;border:1px solid var(--silver);display:flex;align-items:center;justify-content:center;gap:5px;font-size:8px;font-weight:600;letter-spacing:1px;text-transform:uppercase;color:var(--ink)}
.brand i{width:8px;height:8px;background:var(--ink);display:block}
.natural .photo{left:0;top:146px;width:100%;height:286px;background:linear-gradient(200deg,#9a9187,#6b635a 45%,#3a3532)}
.natural .caption{position:absolute;right:14px;bottom:14px;color:var(--paper);font-size:9px;font-weight:500;text-align:right;line-height:12px}

/* inside: who we are */
.about{background:linear-gradient(180deg,#6e6e6e,#585858 55%,#4a4a4a)}
.about .title{position:absolute;left:18px;top:80px;color:var(--paper);font-weight:700;font-size:44px;line-height:44px}
.about .title span{display:block;padding-left:60px}
.about .body{position:absolute;left:18px;right:22px;top:188px;color:#eeeeee;font-size:7.5px;line-height:11px}

/* inside: why planning */
.planning{background:linear-gradient(180deg,#ffffff 0,#ffffff 52%,#e4e4e4 70%,#d2d2d2)}
.planning .title{position:absolute;left:22px;top:88px;line-height:1.05}
.planning .title span{display:block;font-size:16px;font-weight:400}
.planning .title strong{display:block;font-size:24px;font-weight:700}
.benefits{position:absolute;left:22px;right:18px;top:158px;display:grid;grid-template-columns:1fr 1fr;gap:10px 8px}
.benefit{display:flex;align-items:center;gap:5px;font-size:6px;line-height:8px;color:var(--ink-soft)}
.benefit svg{flex:none}
.planning .body{position:absolute;left:22px;right:20px;top:250px;font-size:8px;line-height:12px;color:var(--ink)}
.planning .body p+p{margin-top:8px}

/* inside: landscape services */
.landscape .title{position:absolute;left:20px;top:56px;line-height:1.15}
.landscape .title span{display:block;font-size:15px;font-weight:400}
.landscape .title span:nth-child(2){padding-left:14px}
.landscape .title strong{display:block;font-size:18px;font-weight:700}
.offer-list{position:absolute;left:20px;right:18px;top:136px;list-style:none}
.offer{position:relative;margin-bottom:12px}
.offer h3{font-size:9.5px;font-weight:500;color:var(--ink)}
.offer ul{list-style:none;font-size:7px;line-height:10px;color:var(--ink-soft);margin-top:2px}
.offer ul li::before{content:"•";margin-right:4px}
.offer .num{position:absolute;right:0;top:-6px;font-size:22px;font-weight:300;color:var(--silver)}
</style>
</head>
<body>

<section class="sheet sheet--outside">
  <div class="panel masonry">
    <p class="eyebrow">Masonry</p>
    <h2 class="title">Concrete</h2>
    <p class="sub">Services</p>
    <ul class="service-list">
      <li>Brick, block &amp; stone masonry</li>
      <li>Chimney &amp; fireplace rebuild / repair</li>
      <li>Stucco restoration</li>
      <li>Concrete slabs, steps &amp; foundations</li>
      <li>Repairs, waterproofing &amp; sealing</li>
    </ul>
    <div class="photo" role="img" aria-label="Stone and timber home with masonry steps and landscaping"></div>
  </div>

  <div class="panel craft">
    <div class="photo photo--top" role="img" aria-label="Stone patio with outdoor kitchen and fire feature"></div>
    <p class="tagline">Reinforce Craftsmanship And Longevity</p>
    <div class="photo photo--mid" role="img" aria-label="Finished stone retaining wall and steps"></div>
    <p class="motto">Plan it right.<br>
      <svg width="12" height="12" viewBox="0 0 12 12"><path d="M2 6.5l2.5 2.5L10 3" fill="none" stroke="#fff" stroke-width="1.6"/></svg>Build it once.</p>
    <p class="web">birchledgerbuilds.com</p>
  </div>

  <div class="panel natural">
    <h2 class="heading"><span>Natural Elements</span><strong>In Motion</strong></h2>
    <div class="brand"><i></i>Birch Ledger</div>
    <div class="photo" role="img" aria-label="Floor-to-ceiling natural stone fireplace in a living room"></div>
    <p class="caption">Premium,<br>Understated Design</p>
  </div>
</section>

<section class="sheet sheet--inside">
  <div class="panel about">
    <h2 class="title">Who<span>We Are</span></h2>
    <p class="body">Birch Ledger is a masonry and landscape company serving northern Minnesota and Wisconsin. We focus on smart planning and outlasting, durable craftsmanship built for a harsh climate, proper drainage, frost protection and solid footings that protect your investment. We specialize in masonry, landscape and outdoor living spaces built to last for many years.</p>
  </div>

  <div class="panel planning">
    <h2 class="title"><span>Why</span><strong>Planning</strong><span>Matters</span></h2>
    <div class="benefits">
      <div class="benefit"><svg width="18" height="18" viewBox="0 0 18 18"><circle cx="9" cy="9" r="8" fill="none" stroke="#555" stroke-width="1"/><path d="M9 4c2 3 3 4.5 3 6a3 3 0 0 1-6 0c0-1.5 1-3 3-6z" fill="#555"/></svg>Drainage &amp; erosion management</div>
      <div class="benefit"><svg width="18" height="18" viewBox="0 0 18 18"><circle cx="9" cy="9" r="8" fill="none" stroke="#555" stroke-width="1"/><path d="M9 4v10M4.7 6.5l8.6 5M13.3 6.5l-8.6 5" stroke="#555" stroke-width="1"/></svg>Frost depth &amp; reinforcement</div>
      <div class="benefit"><svg width="18" height="18" viewBox="0 0 18 18"><circle cx="9" cy="9" r="8" fill="none" stroke="#555" stroke-width="1"/><path d="M5 12h8M6 9.5h6M7 7h4" stroke="#555" stroke-width="1.3"/></svg>Foundations built right</div>
      <div class="benefit"><svg width="18" height="18" viewBox="0 0 18 18"><circle cx="9" cy="9" r="8" fill="none" stroke="#555" stroke-width="1"/><path d="M5 9.5l2.5 2.5L13 6" fill="none" stroke="#555" stroke-width="1.3"/></svg>Long lasting in harsh climates</div>
    </div>
    <div class="body">
      <p>Drainage is the foundation of every successful landscape, hardscape, and masonry project.</p>
      <p>In Northern Minnesota's climate, poor drainage and frost protection lead to failure, damage, and costly disappointment.</p>
    </div>
  </div>

  <div class="panel landscape">
    <h2 class="title"><span>Landscape</span><span>And Outdoor</span><strong>Living Services</strong></h2>
    <ol class="offer-list">
      <li class="offer"><h3>Landscape Design</h3><span class="num">01</span>
        <ul><li>Site planning &amp; layouts</li><li>Plant selection &amp; garden design</li><li>Concept plans &amp; renderings</li></ul></li>
      <li class="offer"><h3>Landscape Installation</h3><span class="num">02</span>
        <ul><li>Planting (trees, shrubs, flowers)</li><li>Sod &amp; seeding</li><li>Mulch, rock, groundcovers</li></ul></li>
      <li class="offer"><h3>Hardscape &amp; Outdoor Living</h3><span class="num">03</span>
        <ul><li>Patios, walkways, retaining walls</li><li>Drip irrigation</li><li>French drains, grading, swales</li></ul></li>
      <li class="offer"><h3>Irrigation &amp; Drainage</h3><span class="num">04</span>
        <ul><li>Sprinkler systems</li><li>Drip irrigation</li><li>French drains, grading, swales</li></ul></li>
      <li class="offer"><h3>Outdoor Lighting</h3>
        <ul><li>Pathway &amp; landscape lighting</li><li>Accent lighting</li></ul></li>
    </ol>
  </div>
</section>

</body>
</html>
```